we can communicate on this, but i want to follow the approach we took on Pellow|Quint & Marsh but i feel the card front needs the black background and the platinum and gold logo. The back? I am open. we can use the same info from PQ&M. Velmora Point is an enhanced equity investment fund - basically a very exclusive boutique hedge fund that uses only stock options. very advanced things. hope you are interested

Contact Information for Business Card

Dr. Lewis T. Brennick, CFA
Scientifique de fusée financière
701.555.0143
LBdoc4490@mailvex.example

4817 Birch Hollow Way W.
West Fargo, ND 58099

No web site

Colors

Designer to choose colors to be used in the design.

Requirements
Nice to have
• I tend to prefer the most visible applications of the logo to include logo and name, the logo version with a black background and the gold and platinum components separated by the black. I see this working well for a single side (logo and name - this is card front to me).
• I am fairly open to other treatments on the reverse side with the data. To me, it makes sense to have a different color rendition of the logo on the reverse and it may be a muted black tone on tone or an oversized portion that would have spot UV. Or, the reverse may play with colors and layout
Should not have
• Other colors = no no
• Decorative font

```html
<!DOCTYPE html>
<html lang="en">
<head>
<meta charset="UTF-8">
<title>Velmora Point – Business Card</title>
<link href="https://fonts.googleapis.com/css2?family=Open+Sans:wght@400;700&display=swap" rel="stylesheet">
<style>
  :root {
    --backdrop: #a2a2a2;
    --card: #050505;
    --gold: #d2a937;
    --platinum: #f2f2f2;
    --muted: #e6e6e6;
  }
  * { margin: 0; padding: 0; box-sizing: border-box; }
  html, body {
    width: 1200px; height: 720px; overflow: hidden;
    background: var(--backdrop);
    font-family: "Open Sans", Arial, sans-serif;
  }
  .sheet {
    position: relative; width: 1200px; height: 720px;
    display: flex; align-items: center; justify-content: center; gap: 40px;
  }
  .card {
    position: relative;
    width: 525px; height: 300px;
    background: var(--card);
    box-shadow: 0 6px 18px rgba(0,0,0,0.35);
    overflow: hidden;
  }

  /* Front */
  .card-front .brand {
    position: absolute; left: 50%; top: 50%;
    transform: translate(-50%, -50%);
    display: flex; align-items: center; gap: 14px;
  }
  .brand-dot {
    width: 44px; height: 44px; border-radius: 50%;
    background: var(--gold); flex: none;
  }
  .brand-name {
    color: var(--platinum); font-weight: 700;
    font-size: 30px; letter-spacing: 1px; text-transform: uppercase;
    white-space: nowrap;
  }

  /* Back */
  .card-back .person {
    position: absolute; left: 38px; top: 44px;
  }
  .person-name {
    color: var(--gold); font-weight: 700; font-size: 21px; line-height: 1.15;
    white-space: nowrap;
  }
  .person-title {
    color: var(--muted); font-size: 14px; margin-top: 2px;
  }
  .contact-list {
    position: absolute; left: 38px; top: 128px;
    list-style: none;
  }
  .contact-list li {
    display: flex; align-items: center; gap: 10px;
    color: var(--muted); font-size: 13.5px; line-height: 1; margin-bottom: 10px;
    white-space: nowrap;
  }
  .contact-list svg { width: 15px; height: 15px; flex: none; }
  .card-back .brand {
    position: absolute; right: 34px; bottom: 34px;
    display: flex; align-items: center; gap: 9px;
  }
  .card-back .brand-dot { width: 26px; height: 26px; }
  .card-back .brand-name { font-size: 17px; }
</style>
</head>
<body>
<main class="sheet">

  <section class="card card-front" aria-label="Card front">
    <div class="brand">
      <span class="brand-dot"></span>
      <span class="brand-name">Velmora Point</span>
    </div>
  </section>

  <section class="card card-back" aria-label="Card back">
    <div class="person">
      <p class="person-name">Dr. Lewis T. Brennick, CFA</p>
      <p class="person-title">Scientifique de fusée financière</p>
    </div>

    <ul class="contact-list">
      <li>
        <svg viewBox="0 0 16 16" fill="none" stroke="var(--gold)" stroke-width="1.6"><rect x="4" y="1.5" width="8" height="13" rx="1.5"/><line x1="7" y1="12" x2="9" y2="12"/></svg>
        701.555.0143
      </li>
      <li>
        <svg viewBox="0 0 16 16" fill="none" stroke="var(--gold)" stroke-width="1.5"><rect x="1.5" y="3.5" width="13" height="9"/><polyline points="1.5,3.5 8,9 14.5,3.5"/></svg>
        LBdoc4490@mailvex.example
      </li>
      <li>
        <svg viewBox="0 0 16 16" fill="var(--gold)"><path d="M8 1a5 5 0 0 0-5 5c0 3.6 5 9 5 9s5-5.4 5-9a5 5 0 0 0-5-5zm0 7a2 2 0 1 1 0-4 2 2 0 0 1 0 4z"/></svg>
        4817 Birch Hollow Way W., West Fargo, ND 58099
      </li>
    </ul>

    <div class="brand">
      <span class="brand-dot"></span>
      <span class="brand-name">Velmora Point</span>
    </div>
  </section>

</main>
</body>
</html>
```